Word template for proposals we send to clients

We want a word template designed based on the look/feel of our website. The website is www.brovanex.com.au and while we have pictures of 2 staff on the website we have pictures of other staff if required

the template will be used to send out proposals to potential clients, therefore it has to be professional, modern and compelling for someone to open

Target Market(s)

B2B

Industry/Entity Type

It Company

Font styles to use
Serif

Colors

Designer to choose colors to be used in the design.

Requirements
Must have
• Same look and feel as website
Nice to have
• Dont know what I am missing so anythign you feel i need to add

```html
<!DOCTYPE html>
<html lang="en">
<head>
<meta charset="utf-8">
<title>Business Proposal – Brovanex Consulting Services</title>
<link href="https://fonts.googleapis.com/css2?family=Questrial&family=Nunito+Sans:wght@400;700&display=swap" rel="stylesheet">
<style>
  :root {
    --backdrop: #b4b8c0;
    --slate: #2f3c45;
    --lime: #b5c214;
    --leaf: #5c9232;
    --white: #ffffff;
    --muted: #55636d;
    --rule: #4a5862;
  }
  * { margin: 0; padding: 0; box-sizing: border-box; }
  html, body {
    width: 1200px; height: 1200px; overflow: hidden;
    background: var(--backdrop);
  }
  .proposal-cover {
    position: absolute; left: 170px; top: 42px;
    width: 860px; height: 1116px;
    background: var(--slate);
    overflow: hidden;
    font-family: "Questrial", sans-serif;
    color: var(--white);
    box-shadow: 0 6px 18px rgba(0,0,0,0.25);
  }
  .accent-band {
    position: absolute; left: 654px; top: 0; width: 151px; height: 1116px;
    background: var(--lime);
  }
  .accent-band-lower {
    position: absolute; left: 654px; top: 842px; width: 151px; height: 274px;
    background: var(--leaf);
  }
  .brand { position: absolute; left: 60px; top: 66px; }
  .brand-name {
    font-size: 36px; line-height: 1; color: var(--lime); letter-spacing: 0.5px;
  }
  .brand-tagline {
    font-size: 17px; letter-spacing: 1.2px; margin-top: 6px; color: var(--white);
  }
  .company-contact {
    position: absolute; left: 329px; top: 77px;
    font-family: "Nunito Sans", sans-serif;
    font-size: 7.5px; line-height: 11px; color: var(--muted); text-transform: uppercase;
  }
  .company-contact .web { margin-top: 11px; }
  .title { position: absolute; left: 58px; top: 330px; }
  .title-kicker { font-size: 41px; line-height: 1; letter-spacing: 0.5px; }
  .title-main {
    font-size: 86px; line-height: 1; color: var(--lime); margin-top: 8px; letter-spacing: 1px;
  }
  .hero-photo {
    position: absolute; left: 0; top: 480px; width: 860px; height: 362px;
    background: linear-gradient(90deg, #5c6e80 0%, #cfe0ea 18%, #eef2f4 45%, #dfe6ea 70%, #8fa9b5 100%);
  }
  .hero-tint {
    position: absolute; left: 654px; top: 480px; width: 151px; height: 362px;
    background: var(--lime); opacity: 0.6;
  }
  .details {
    position: absolute; top: 900px;
    font-family: "Nunito Sans", sans-serif;
  }
  .details-client { left: 58px; }
  .details-dates { left: 340px; }
  .label { font-size: 12.5px; font-weight: 700; color: var(--lime); line-height: 16px; }
  .recipient { font-family: "Questrial", sans-serif; font-size: 17px; line-height: 22px; }
  .client-block { margin-top: 18px; font-size: 12.5px; line-height: 16px; }
  .client-block strong { font-weight: 700; }
  .date-value { font-size: 13px; line-height: 17px; letter-spacing: 0.5px; }
  .date-group + .date-group { margin-top: 22px; }
  .confidentiality {
    position: absolute; left: 58px; top: 1050px; width: 520px;
    border-top: 1px solid var(--rule); padding-top: 6px;
    font-family: "Nunito Sans", sans-serif;
    font-size: 7.5px; line-height: 10px; color: var(--muted);
  }
  .confidentiality strong { font-weight: 700; display: block; }
</style>
</head>
<body>
  <main class="proposal-cover">
    <div class="accent-band"></div>
    <div class="accent-band-lower"></div>

    <header class="brand">
      <div class="brand-name">Brovanex</div>
      <div class="brand-tagline">CONSULTING&nbsp; SERVICES</div>
    </header>

    <address class="company-contact">
      Lvl 9/212 Harlow St, Melbourne, VIC, 3000, Australia<br>
      1300 47 21 63 / info@brovanex.com.au
      <div class="web">www.brovanex.com.au</div>
    </address>

    <h1 class="title">
      <div class="title-kicker">BUSINESS</div>
      <div class="title-main">PROPOSAL</div>
    </h1>

    <div class="hero-photo" role="img" aria-label="Photo of a consultant standing in a bright office with colleagues meeting at a table behind her"></div>
    <div class="hero-tint"></div>

    <section class="details details-client">
      <div class="label">Prepared for:</div>
      <div class="recipient">Daniel Marlowe</div>
      <div class="client-block">
        <strong>Tidewell Partners LLC</strong><br>
        48 Quarry Lane, Riverton, 4012<br>
        P: 1300 552 019 · E hello@tidewellpartners.com
      </div>
    </section>

    <section class="details details-dates">
      <div class="date-group">
        <div class="label">Proposal Issued:</div>
        <div class="date-value">11.11.2018</div>
      </div>
      <div class="date-group">
        <div class="label">Proposal Valid to:</div>
        <div class="date-value">01.12.2018</div>
      </div>
    </section>

    <footer class="confidentiality">
      <strong>Statement of Confidentiality</strong>
      This proposal and supporting materials contain confidential and proprietary business information of Brovanex. These materials
      may be printed or photocopied for use in evaluating the proposed project, but are not to be shared with other parties.
    </footer>
  </main>
</body>
</html>
```